Web Design Project

We have a website in beta that needs updating and are looking for a freash new look for the Home page including Logo.
Our company is called " Pim Sa Ox " we specialize in classified advertising using video. Our consumers will be businesses selling a product or service. Please visit www.pimsaox.com
Our aim past this point is to engage a developer to write the code based on the best design. Our target market is the U.S and I have included some of the landing pages to give you a better idea of what we are trying to acheive

http://www.pimsaox.com/
http://www.pimsaox.com/cars_home.php
http://www.pimsaox.com/boats.php
http://www.pimsaox.com/electronic.php
http://www.pimsaox.com/realestate.php
http://www.pimsaox.com/roommates.php

Target Market(s)

20-35 yr old people who are connected to the internet via mobile phone and use social media on a daily/weekly basis

Industry/Entity Type

Advertising

Requirements
Must have
• We would like to use lots of images to convey it is a video driven website business
Nice to have
• Logo to incorporate same theme of website ( ie ) you are here to watch videos of thinhs to buy & sell
Should not have
• This is to be a freash new site with large type and bold fonts

```html
<!DOCTYPE html>
<html lang="en">
<head>
<meta charset="utf-8">
<title>Pim Sa Ox – Real Estate</title>
<link href="https://fonts.googleapis.com/css2?family=Oswald:wght@300;400;600&display=swap" rel="stylesheet">
<style>
:root{
  --red:#e0261f;
  --red-dark:#b5140f;
  --charcoal:#2b2b2b;
  --dark:#3a3a3a;
  --frame:#8d8d8d;
  --panel:#e6e6e6;
  --text:#222;
  --white:#fff;
}
*{margin:0;padding:0;box-sizing:border-box}
html,body{width:909px;height:1200px;overflow:hidden;background:var(--white)}
body{position:relative;font-family:Arial,Helvetica,sans-serif;color:var(--text);font-size:12px}
.abs{position:absolute}
.cond{font-family:'Oswald',sans-serif}
.account{right:14px;top:14px;font-size:11.5px}
.navbar{left:20px;top:45px;width:877px;height:51px;background:linear-gradient(#4a4a4a,#262626);border-radius:4px;border-bottom:3px solid #111}
.brand{left:35px;top:34px;width:170px;height:71px;background:var(--dark);border-radius:6px;padding:4px}
.brand-inner{width:100%;height:58px;background:var(--white);border-radius:4px;display:flex;align-items:center;justify-content:center;font-family:'Oswald',sans-serif;font-weight:600;font-size:30px;color:var(--charcoal)}
.nav{left:228px;top:55px;display:flex;gap:0}
.nav a{font-family:'Oswald',sans-serif;font-weight:300;font-size:18px;color:var(--white);text-decoration:none;margin-right:32px;letter-spacing:-.3px}
.nav a.active{color:#bbb}
.headline{left:0;width:909px;top:126px;text-align:center;font-family:'Oswald',sans-serif;font-weight:300;font-size:25px;letter-spacing:-1px;color:var(--charcoal)}
.headline b{font-weight:600;color:var(--red)}
.searchbar{left:72px;top:179px;width:796px;height:45px;background:var(--charcoal);border-radius:10px}
.searchbar .field{position:absolute;left:18px;top:8px;width:597px;height:29px;background:var(--white);border:1px solid #ccc;font-size:11.5px;color:#666;padding:8px 9px}
.searchbar .go{position:absolute;left:629px;top:6px;width:156px;height:32px;background:linear-gradient(#f24a3f,var(--red-dark));border-radius:10px;color:var(--white);font-family:'Oswald',sans-serif;font-weight:600;font-size:19px;text-align:center;line-height:31px}
.promo{left:130px;top:244px;width:693px;height:100px;background:#7a7a7a;border-radius:6px;padding:7px}
.promo-inner{position:relative;width:100%;height:100%;background:#1e1e1e;overflow:hidden}
.promo-art{position:absolute;left:0;top:0;width:450px;height:86px;background:linear-gradient(90deg,#d4361d,#f3b21f 35%,#c63217 60%,#1e1e1e)}
.promo-copy{position:absolute;right:5px;top:4px;text-align:right;color:var(--white);font-size:19px;line-height:20px}
.promo-offer{position:absolute;left:475px;top:50px;color:var(--red);font-size:15px;line-height:16px}
.promo-brand{position:absolute;right:5px;bottom:3px;color:var(--white);font-weight:bold;font-size:11px;letter-spacing:1.5px}
.section-title{left:81px;top:370px;font-family:'Oswald',sans-serif;font-weight:400;font-size:20px;letter-spacing:-.8px}
.player{left:74px;top:401px;width:510px;height:283px;background:#999;border-radius:9px;padding:9px}
.player-screen{position:relative;width:100%;height:100%;background:var(--charcoal);border-radius:5px}
.player-video{position:absolute;left:21px;top:14px;width:458px;height:212px;background:linear-gradient(#1d3a8a,#556 45%,#2a8fd4 75%,#3bb7ee)}
.player-track{position:absolute;left:14px;top:230px;width:464px;height:4px;background:#555}
.player-knob{position:absolute;left:9px;top:226px;width:11px;height:11px;border-radius:50%;background:#ddd}
.player-ctrl{position:absolute;left:14px;top:240px;width:464px;height:24px;color:#ccc;font-size:8px}
.thumb{width:108px;height:94px;background:#999;border-radius:6px;padding:7px}
.thumb-inner{position:relative;width:100%;height:100%;border:3px solid #555;border-radius:3px}
.play{position:absolute;left:50%;top:50%;width:30px;height:30px;margin:-15px 0 0 -15px}
.add-btn{left:71px;top:921px;width:185px;height:35px;background:var(--charcoal);padding:3px;}
.add-btn span{display:block;height:100%;background:var(--red);color:var(--white);font-size:12px;text-align:center;line-height:29px}
.side-head{left:624px;top:401px;width:267px;height:32px;background:var(--dark);border-radius:6px;border-left:6px solid #111;color:var(--white);font-family:'Oswald',sans-serif;font-weight:300;font-size:19px;padding:1px 18px}
.tab{top:453px;height:26px;border-radius:6px 6px 0 0;font-size:13.5px;text-align:center;line-height:26px}
.tab.on{left:624px;width:87px;background:var(--panel)}
.tab.off{left:715px;width:87px;background:#eee;border:1px solid #ddd;border-bottom:0;line-height:22px;height:23px;top:454px}
.side-panel{left:624px;top:478px;width:265px;height:272px;background:var(--panel);border-radius:0 6px 6px 6px}
.checks{left:643px;top:504px;font-size:11.5px;display:flex;gap:16px}
.box{display:inline-block;width:11px;height:11px;border:1px solid #888;background:#fff;vertical-align:-2px;margin-right:5px}
.row{left:646px;width:230px;height:24px;font-size:11.5px}
.row label{position:absolute;left:0;top:6px}
.row .sel{position:absolute;left:65px;top:0;width:166px;height:23px;background:#f2f2f2;border:1px solid #ddd}
.row .sel i{position:absolute;right:4px;top:5px;width:11px;height:11px;border:1px solid #888;background:#fff}
.row .sel i::after{content:"";position:absolute;left:2px;top:3px;border:3px solid transparent;border-top-color:#333}
.side-go{left:763px;top:703px;width:109px;height:28px;background:var(--red);border-radius:7px;color:var(--white);font-size:12px;text-align:center;line-height:28px;box-shadow:0 0 0 2px #fff}
.footer{left:7px;top:1039px;width:895px;height:82px;background:#eaeaea;border-radius:6px}
.footer-inner{position:absolute;left:11px;top:8px;width:873px;height:67px;background:linear-gradient(#4a4a4a,#2a2a2a);border-radius:4px;color:var(--white)}
.footer-links{position:absolute;left:31px;top:29px;font-size:11.5px}
.footer-contact{position:absolute;left:555px;top:6px;width:310px;font-size:10px;line-height:12px;color:#ddd}
.footer-contact h3{font-size:13px;color:var(--white);line-height:15px}
.copy{left:0;width:909px;top:1145px;text-align:center;font-size:10.5px}
.terms{left:0;width:909px;top:1169px;text-align:center;font-size:10.5px}
.terms a{color:var(--red);text-decoration:none}
</style>
</head>
<body>
<div class="abs account">member login · register</div>
<div class="abs navbar"></div>
<div class="abs brand"><div class="brand-inner">Pim Sa Ox</div></div>
<nav class="abs nav">
  <a href="#">CARS</a><a href="#">BOATS</a><a href="#" class="active">REAL ESTATE</a><a href="#">ELECTRONICS</a><a href="#">ROOMMATE</a><a href="#">TOYS</a><a href="#">FASION</a><a href="#">OTHER</a>
</nav>

<h1 class="abs headline">BUY AND SELL THROUGH THE <b>#1 VIDEO CLASSIFIEDS</b></h1>

<div class="abs searchbar">
  <div class="field">Search or Type your Keyword Here ...</div>
  <div class="go">search</div>
</div>

<div class="abs promo">
  <div class="promo-inner">
    <div class="promo-art" role="img" aria-label="Sneaker advertisement artwork with a high-top shoe on a psychedelic orange and yellow backdrop"></div>
    <div class="promo-copy">Stridewell Classic<br>High-Top</div>
    <div class="promo-offer">Free Shipping<br>Shop Now &gt;</div>
    <div class="promo-brand">STRIDEWELL</div>
  </div>
</div>

<h2 class="abs section-title">Real Estate Listings</h2>

<div class="abs player">
  <div class="player-screen">
    <div class="player-video" role="img" aria-label="Video still of a two-storey house with a lit swimming pool at dusk"></div>
    <div class="player-track"></div>
    <div class="player-knob"></div>
    <svg class="player-ctrl" viewBox="0 0 464 24">
      <rect x="6" y="7" width="3" height="10" fill="#ccc"/><rect x="12" y="7" width="3" height="10" fill="#ccc"/>
      <path d="M34 10h3l4-3v10l-4-3h-3z" fill="#ccc"/>
      <text x="58" y="15" fill="#fff" font-size="8" font-family="Arial">00:00 <tspan fill="#aaa">/ 18:50</tspan></text>
      <circle cx="386" cy="12" r="4" fill="none" stroke="#ccc" stroke-width="2"/>
      <circle cx="408" cy="12" r="4" fill="#ccc"/>
      <rect x="424" y="8" width="12" height="7" fill="none" stroke="#fff" stroke-width="2"/>
      <rect x="446" y="7" width="13" height="9" fill="none" stroke="#ccc" stroke-width="1.5"/>
    </svg>
  </div>
</div>

<div class="abs thumb" style="left:74px;top:699px"><div class="thumb-inner" style="background:linear-gradient(#27407a,#b07a3a 60%,#6d7d2a)" role="img" aria-label="Modern home at sunset"><svg class="play" viewBox="0 0 30 30"><circle cx="15" cy="15" r="14" fill="#fff" stroke="#222" stroke-width="2"/><path d="M11 8l11 7-11 7z" fill="#222"/></svg></div></div>
<div class="abs thumb" style="left:208px;top:699px"><div class="thumb-inner" style="background:linear-gradient(#9bb4d8,#e8dcc8 55%,#3aa7d8)" role="img" aria-label="Villa with pool"><svg class="play" viewBox="0 0 30 30"><circle cx="15" cy="15" r="14" fill="#fff" stroke="#222" stroke-width="2"/><path d="M11 8l11 7-11 7z" fill="#222"/></svg></div></div>
<div class="abs thumb" style="left:342px;top:699px"><div class="thumb-inner" style="background:linear-gradient(#8fb5e0,#e6e6e6 55%,#3f7a2c)" role="img" aria-label="White family house with lawn"><svg class="play" viewBox="0 0 30 30"><circle cx="15" cy="15" r="14" fill="#fff" stroke="#222" stroke-width="2"/><path d="M11 8l11 7-11 7z" fill="#222"/></svg></div></div>
<div class="abs thumb" style="left:476px;top:699px"><div class="thumb-inner" style="background:linear-gradient(#c8d4e0,#8a2a22 50%,#4b6a2c)" role="img" aria-label="Red brick house"><svg class="play" viewBox="0 0 30 30"><circle cx="15" cy="15" r="14" fill="#fff" stroke="#222" stroke-width="2"/><path d="M11 8l11 7-11 7z" fill="#222"/></svg></div></div>
<div class="abs thumb" style="left:74px;top:811px"><div class="thumb-inner" style="background:linear-gradient(#2a2a2a,#6a3a30 50%,#3a3a3a)" role="img" aria-label="Product close-up"><svg class="play" viewBox="0 0 30 30"><circle cx="15" cy="15" r="14" fill="#fff" stroke="#222" stroke-width="2"/><path d="M11 8l11 7-11 7z" fill="#222"/></svg></div></div>
<div class="abs thumb" style="left:208px;top:811px"><div class="thumb-inner" style="background:linear-gradient(#4aa8e8,#dfe6ee 50%,#1f5f8a)" role="img" aria-label="Motor yacht on the water"><svg class="play" viewBox="0 0 30 30"><circle cx="15" cy="15" r="14" fill="#fff" stroke="#222" stroke-width="2"/><path d="M11 8l11 7-11 7z" fill="#222"/></svg></div></div>
<div class="abs thumb" style="left:342px;top:811px"><div class="thumb-inner" style="background:linear-gradient(90deg,#c23a2a,#2a8a3a 35%,#7a2aa0 65%,#d8a02a)" role="img" aria-label="Colourful action figure toys"><svg class="play" viewBox="0 0 30 30"><circle cx="15" cy="15" r="14" fill="#fff" stroke="#222" stroke-width="2"/><path d="M11 8l11 7-11 7z" fill="#222"/></svg></div></div>
<div class="abs thumb" style="left:476px;top:811px"><div class="thumb-inner" style="background:linear-gradient(90deg,#b8531e,#eed8b8 60%,#f4f0e8)" role="img" aria-label="Bright room interior"><svg class="play" viewBox="0 0 30 30"><circle cx="15" cy="15" r="14" fill="#fff" stroke="#222" stroke-width="2"/><path d="M11 8l11 7-11 7z" fill="#222"/></svg></div></div>

<div class="abs add-btn"><span>ADD PRODUCT TO LISTING</span></div>

<div class="abs side-head">REAL ESTATE</div>
<div class="abs side-panel"></div>
<div class="abs tab on">Buyer</div>
<div class="abs tab off">Seller</div>
<div class="abs checks"><span><i class="box"></i>residential</span><span><i class="box"></i>commercial</span></div>
<div class="abs row" style="top:529px"><label>Type:</label><div class="sel"><i></i></div></div>
<div class="abs row" style="top:562px"><label>Property:</label><div class="sel"><i></i></div></div>
<div class="abs row" style="top:596px"><label>State</label><div class="sel"><i></i></div></div>
<div class="abs row" style="top:629px"><label>City</label><div class="sel"><i></i></div></div>
<div class="abs row" style="top:663px"><label>Suburb:</label><div class="sel"><i></i></div></div>
<div class="abs side-go">SEARCH</div>

<footer class="abs footer">
  <div class="footer-inner">
    <div class="footer-links">Home · About us · Sell · Search · How It Works · Help · Advertise With Us</div>
    <div class="footer-contact"><h3>Contact Us</h3>Need assistance? Have a question that isn't answered in our help sections? You can contact support by visiting our contact us page.</div>
  </div>
</footer>
<div class="abs copy">Copyright © 2013 Pim Sa Ox. All Rights Reserved.</div>
<div class="abs terms">Use of this Web site constitutes acceptance of the <a href="#">User Agreement</a> and <a href="#">Privacy Policy</a>. Designated trademarks and brands are the property of their respective owners.</div>
</body>
</html>
```